Dr. Lumora needs a design for its website!

*Only need the design, coding is not required.
*Need desktop version ($500) and mobile/tablet version ($200)
*The attached files are not the exact layout we want, they are just for you to know what information should be included in those pages.
*The function of our website is like www.qavlo.hk
*For the background picture, prefer a lively picture and chinese people in it, NOT necessarily need a doctor or sick person in the picture

***Don't just copy the layout from the attachments or from the reference website, we are looking for creative ideas, non-ordinary designs!!!****

We are developing a website for the public to search a doctor by different criteria. At the initial stage, we need 4 pages to start with and other pages at later stage. I have attached the general idea of these pages but not necessarily to be exactly the same, I am looking for some new ideas.

This website needs a professional, modern, simple and user friendly design. The main color to be used in the website will be same as the color (R:0 G:139 B:205) used in our logo (see attached). We don't have any particular thoughts for the other color and the font to be used in the website. Can try to use circle outline for the icon in the navigation bar.

1. Home: will include 4 sections (see attached)

2. Doctor's details (see attached)

3. Health information: will include a short descriptions of this Health Info page and 5 sections (see attached)

4. News (see attached)

Reason: Not too many suitable designs to choose from and need more time to go through the designs

All

Medical

4 page

• must not be same as or looks too much like www.qavlo.hk
• prefer not to use black and red color

```html
<!DOCTYPE html>
<html lang="en">
<head>
<meta charset="utf-8">
<title>Dr. Lumora</title>
<link rel="stylesheet" href="https://fonts.googleapis.com/css2?family=Open+Sans:wght@400;600;700&family=Montserrat:wght@400;500&display=swap">
<style>
:root{
  --brand:#008bcd;
  --brand-dark:#0077b3;
  --ink:#555b61;
  --ink-dark:#222;
  --muted:#9a9a9a;
  --panel:#efefef;
  --white:#fff;
}
*{box-sizing:border-box;margin:0;padding:0}
html,body{width:1200px;height:3077px;overflow:hidden}
body{position:relative;background:var(--white);font-family:"Open Sans",Arial,sans-serif;color:var(--ink)}
.abs{position:absolute}
.btn{position:absolute;display:flex;align-items:center;justify-content:center;background:var(--brand);color:var(--white);font-size:19px;letter-spacing:.3px}
.title{position:absolute;left:0;width:1200px;text-align:center;font-size:38px;color:#555;font-weight:400;letter-spacing:.5px}
.title b,.accent{color:var(--brand);font-weight:400}

/* hero */
.hero{left:0;top:0;width:1200px;height:697px;background:linear-gradient(100deg,#d8dde2 0%,#eef1f3 35%,#b9c8d6 70%,#8ba6c2 100%)}
.nav{left:0;top:0;width:1200px;height:74px;border-bottom:1px solid rgba(255,255,255,.6);font-family:Montserrat,Arial,sans-serif}
.nav-item{position:absolute;top:28px;font-size:15px;color:#222}
.nav-item.active{color:var(--brand)}
.nav-underline{left:78px;top:70px;width:86px;height:4px;background:var(--brand)}
.lang{top:26px;left:968px;font-size:18px;color:var(--brand)}
.lang span{color:#333;margin-left:14px}
.brand-mark{left:320px;top:170px;width:170px;height:170px;border-radius:50%;background:var(--brand)}
.brand-name{left:510px;top:205px;font-size:94px;font-weight:600;color:var(--brand);letter-spacing:-1px}
.call{left:322px;top:414px;font-size:40px;font-weight:700;color:#111;display:flex;align-items:center;gap:22px}
.call .ring{width:66px;height:66px;border:3px solid #111;border-radius:50%;display:flex;align-items:center;justify-content:center}

/* search */
.search{left:78px;top:630px;width:1044px;height:293px}
.search-title{left:78px;top:690px;width:1044px;text-align:center;font-size:38px;color:var(--white)}
.field{position:absolute;height:50px;background:#f2f2f2;font-size:14px;color:#444;padding-left:14px;display:flex;align-items:center}
.field .caret{position:absolute;right:12px;top:20px;width:0;height:0;border-left:9px solid transparent;border-right:9px solid transparent;border-top:11px solid var(--brand)}
.radio{display:inline-block;width:14px;height:14px;border:2px solid var(--brand);border-radius:50%;margin:0 8px 0 14px;position:relative}
.radio.on::after{content:"";position:absolute;left:2px;top:2px;width:6px;height:6px;border-radius:50%;background:var(--brand)}
.field-btn{position:absolute;height:50px;background:var(--white);color:var(--brand);font-size:20px;display:flex;align-items:center;justify-content:center}

/* welcome */
.lead{position:absolute;text-align:center;font-size:14px;line-height:27px;color:var(--muted)}

/* member */
.member{left:78px;top:1345px;width:1044px;height:415px;background:var(--panel)}
.member-photo{left:92px;top:1345px;width:328px;height:415px;background:linear-gradient(180deg,#e9e9e9,#f5f5f5 60%,#dfe4e8)}
.perks{left:484px;top:1468px;list-style:none;font-size:15px;color:#333}
.perks li{height:31px;display:flex;align-items:center}
.perks li::before{content:"";width:14px;height:14px;border:2px solid var(--brand);border-radius:50%;margin-right:18px;box-shadow:inset 0 0 0 2px #efefef;background:var(--brand)}
.band{left:78px;top:1760px;width:1044px;height:137px;background:var(--brand)}
.band-text{left:107px;top:1805px;width:720px;font-size:17px;line-height:28px;color:var(--white)}
.band-btn{left:847px;top:1803px;width:248px;height:55px;border:2px solid var(--white);color:var(--white);font-size:19px;display:flex;align-items:center;justify-content:center}

/* doctor list */
.doctors{left:78px;top:1897px;width:1044px;height:523px;background:linear-gradient(90deg,#ececec,#e4e7ea 50%,#eeeeee)}
.table{left:90px;top:2022px;width:1020px;border-collapse:collapse;font-size:13px;color:#333}
.table th{background:var(--brand);color:var(--white);font-weight:400;font-size:17px;text-align:left;height:62px;padding-left:20px;border-right:2px solid #36a4da}
.table th:last-child{border-right:0}
.table td{height:51px;padding-left:18px;border-bottom:2px solid var(--brand);background:rgba(255,255,255,.75)}
.table td.name{padding-left:8px}
.avatar{display:inline-block;width:38px;height:38px;border-radius:50%;background:#c9b6a6;border:2px solid #999;vertical-align:middle;margin-right:12px}
.table td.book{color:var(--brand)}
.view-all{left:0;top:2316px;width:1200px;text-align:center;font-size:15px;color:var(--brand)}

/* health */
.info-photo{position:absolute;width:217px;height:155px;border:1px solid #ddd}
.info-title{position:absolute;font-size:19px;color:#333}
.info-text{position:absolute;width:262px;font-size:14px;line-height:25px;color:var(--muted)}

/* footer */
.footer{left:0;top:2857px;width:1200px;height:220px;background:var(--brand);color:var(--white)}
.foot-nav{position:absolute;top:2890px;font-size:15px;color:var(--white)}
.foot-home{left:78px;top:2878px;width:92px;height:45px;border:2px solid var(--white);color:var(--white);font-size:15px;display:flex;align-items:center;justify-content:center}
.social{left:1076px;top:2877px;width:46px;height:46px;border-radius:50%;background:var(--white)}
.divider{left:78px;top:2950px;width:1044px;height:1px;background:rgba(255,255,255,.35)}
.foot-contact{position:absolute;font-size:14px;line-height:22px;color:var(--white)}
.icon-disc{position:absolute;width:50px;height:50px;border-radius:50%;background:var(--white);display:flex;align-items:center;justify-content:center}
</style>
</head>
<body>

<!-- hero -->
<div class="abs hero" role="img" aria-label="Bright clinic scene with a doctor working at a computer"></div>
<nav class="abs nav">
  <span class="nav-item active" style="left:97px">HOME</span>
  <span class="nav-item" style="left:194px">DOCTOR LIST</span>
  <span class="nav-item" style="left:340px">HEALTH INFO</span>
  <span class="nav-item" style="left:491px">NEWS</span>
  <span class="nav-item" style="left:586px">ABOUT US</span>
  <span class="nav-item" style="left:715px">CONTACT US</span>
  <span class="abs lang">English<span>繁</span><span>简</span></span>
</nav>
<div class="abs nav-underline"></div>

<div class="abs brand-mark"></div>
<div class="abs brand-name">Dr. Lumora</div>
<div class="abs call">CALL US
  <span class="ring"><svg width="32" height="32" viewBox="0 0 24 24"><path d="M6.6 10.8a15.1 15.1 0 0 0 6.6 6.6l2.2-2.2a1 1 0 0 1 1-.25 11.4 11.4 0 0 0 3.6.57 1 1 0 0 1 1 1V20a1 1 0 0 1-1 1A17 17 0 0 1 3 4a1 1 0 0 1 1-1h3.5a1 1 0 0 1 1 1c0 1.25.2 2.45.57 3.57a1 1 0 0 1-.25 1z" fill="#111"/></svg></span>
  123-456-7890</div>
<div class="btn" style="left:466px;top:494px;width:268px;height:62px">BOOK APPOINTMENT</div>

<!-- search -->
<svg class="abs search" viewBox="0 0 1044 293" preserveAspectRatio="none"><polygon points="0,0 1044,0 1044,252 522,293 0,252" fill="#008bcd"/></svg>
<div class="abs search-title">SEARCH</div>
<div class="field" style="left:90px;top:757px;width:261px">Doctor's Name:</div>
<div class="field" style="left:361px;top:757px;width:258px">Symptoms :<span class="caret"></span></div>
<div class="field" style="left:632px;top:757px;width:258px">Gender:<span class="radio on"></span>Male<span class="radio"></span>Female</div>
<div class="field-btn" style="left:900px;top:757px;width:210px">RESET</div>
<div class="field" style="left:90px;top:818px;width:261px">Specialist:<span class="caret"></span></div>
<div class="field" style="left:361px;top:818px;width:258px">District:<span class="caret"></span></div>
<div class="field" style="left:632px;top:818px;width:258px">Phone Number:</div>
<div class="field-btn" style="left:900px;top:818px;width:210px">SEARCH</div>

<!-- welcome -->
<div class="title" style="top:1044px">WELCOME TO <b>DR. LUMORA</b></div>
<p class="lead" style="left:160px;top:1110px;width:880px">Lorem ipsum is the dummy text It has survived not only five centuries, but also the leap into electronic typesetting, remaining essentially unchanged. Lorem Ipsum is simply dummy text of the printing and typesetting industry. Lorem Ipsum has been the industry's standard dummy text ever since the 1500s, when an unknown printer took a galley of type and scrambled it to make a type specimen book. It has survived.</p>
<div class="btn" style="left:502px;top:1224px;width:195px;height:56px">KNOW MORE</div>

<!-- member -->
<div class="abs member"></div>
<div class="abs member-photo" role="img" aria-label="Smiling female doctor holding a clipboard and pen"></div>
<div class="abs" style="left:484px;top:1402px;font-size:38px;color:#555">BECOME A <span class="accent">DR. LUMORA MEMBER</span></div>
<ul class="abs perks">
  <li>First - hand Health News</li>
  <li>Exclusive promotions</li>
  <li>Instant health advices</li>
  <li>Free Health Seminars/ talks</li>
  <li>Priority Doctor appointments And More!</li>
</ul>
<div class="btn" style="left:484px;top:1641px;width:199px;height:55px">MEMBER LOGIN</div>

<div class="abs band"></div>
<p class="abs band-text">Lorem ipsum is the dummy text It has survived not only five centuries, but also the into electronic typesetting, remaining essentially unchanged.</p>
<div class="abs band-btn">BOOK APPOINTMENT</div>

<!-- doctor list -->
<div class="abs doctors" role="img" aria-label="Faint background of a doctor at a desk"></div>
<div class="title" style="top:1956px">DOCTOR <b>LIST</b></div>
<table class="abs table">
  <tr><th style="width:166px">Doctor Name</th><th style="width:124px">Gender</th><th style="width:155px">Speciallist</th><th style="width:270px">Clinic Address</th><th style="width:140px">Phone Num</th><th></th></tr>
  <tr><td class="name"><span class="avatar"></span>Dr. Lorem</td><td>Female</td><td>Ophthalmology</td><td>101 - lorem ipsum is simple dummy</td><td>123 456 7890</td><td class="book">BooK Appointment</td></tr>
  <tr><td class="name"><span class="avatar"></span>Dr. Lorem</td><td>Male</td><td>Ophthalmology</td><td>101 - lorem ipsum is simple dummy</td><td>123 456 7890</td><td class="book">BooK Appointment</td></tr>
  <tr><td class="name"><span class="avatar"></span>Dr. Lorem</td><td>Female</td><td>Ophthalmology</td><td>101 - lorem ipsum is simple dummy</td><td>123 456 7890</td><td class="book">BooK Appointment</td></tr>
  <tr><td class="name"><span class="avatar"></span>Dr. Lorem</td><td>Male</td><td>Ophthalmology</td><td>101 - lorem ipsum is simple dummy</td><td>123 456 7890</td><td class="book">BooK Appointment</td></tr>
</table>
<div class="abs view-all">+ VIEW ALL</div>

<!-- health information -->
<div class="title" style="top:2477px">HEALTH <b>INFORMATION</b></div>
<p class="lead" style="left:150px;top:2535px;width:900px;color:#777">Lorem Ipsum is simply dummy text of the printing and typesetting industry. Lorem Ipsum has been the industry's standard dummy text ever since the 1500s, when an unknown printer took a galley of type and scrambled it to make a type specimen book. It has survived not only five centuries, but also the leap into electronic typesetting, remaining</p>

<div class="info-photo" style="left:78px;top:2638px;background:linear-gradient(135deg,#dfe8ee,#f7f9fa 60%,#cfdbe3)" role="img" aria-label="Male doctor in white coat with stethoscope"></div>
<div class="info-title" style="left:316px;top:2636px">Madical <span class="accent">Emergency Team</span></div>
<p class="info-text" style="left:316px;top:2670px">Lorem Ipsum is simply dummy text of the printing and typesetting industry...</p>
<div class="btn" style="left:318px;top:2732px;width:166px;height:51px;font-size:18px">CONTACT US</div>

<div class="info-photo" style="left:605px;top:2638px;background:linear-gradient(135deg,#e6e2dc,#f8f6f3 55%,#d9d4cc)" role="img" aria-label="Female doctor working at a laptop"></div>
<div class="info-title" style="left:845px;top:2636px">Madical Non-<span class="accent">Emergency Team</span></div>
<p class="info-text" style="left:845px;top:2670px">Lorem Ipsum is simply dummy text of the printing and typesetting industry...</p>
<div class="btn" style="left:847px;top:2732px;width:166px;height:51px;font-size:18px">CONTACT US</div>

<!-- footer -->
<footer class="abs footer"></footer>
<div class="abs foot-home">Home</div>
<span class="foot-nav" style="left:198px">Doctor List</span>
<span class="foot-nav" style="left:315px">Health Info</span>
<span class="foot-nav" style="left:440px">News</span>
<span class="foot-nav" style="left:524px">About Us</span>
<span class="foot-nav" style="left:636px">Contact Us</span>
<div class="abs social"></div>
<div class="abs divider"></div>
<div class="foot-contact" style="left:80px;top:2966px;font-size:18px">Contact Us</div>

<div class="icon-disc" style="left:78px;top:3000px"><svg width="22" height="28" viewBox="0 0 24 30"><path d="M12 0a10 10 0 0 0-10 10c0 7.5 10 20 10 20s10-12.5 10-20A10 10 0 0 0 12 0zm0 14a4 4 0 1 1 0-8 4 4 0 0 1 0 8z" fill="#d0202e"/></svg></div>
<div class="foot-contact" style="left:148px;top:3003px;width:190px">101- Lorem Ipsum is text of printing and type.</div>

<div class="icon-disc" style="left:346px;top:3000px;background:transparent;border:2px solid #fff"><svg width="22" height="22" viewBox="0 0 24 24"><path d="M6.6 10.8a15.1 15.1 0 0 0 6.6 6.6l2.2-2.2a1 1 0 0 1 1-.25 11.4 11.4 0 0 0 3.6.57 1 1 0 0 1 1 1V20a1 1 0 0 1-1 1A17 17 0 0 1 3 4a1 1 0 0 1 1-1h3.5a1 1 0 0 1 1 1c0 1.25.2 2.45.57 3.57a1 1 0 0 1-.25 1z" fill="#fff"/></svg></div>
<div class="foot-contact" style="left:416px;top:3014px">123-456-7890</div>

<div class="icon-disc" style="left:608px;top:3000px"><svg width="24" height="18" viewBox="0 0 24 18"><rect x="1" y="1" width="22" height="16" rx="2" fill="none" stroke="#008bcd" stroke-width="2"/><path d="M2 2l10 8 10-8" fill="none" stroke="#008bcd" stroke-width="2"/></svg></div>
<div class="foot-contact" style="left:678px;top:3014px">info@drlumora.net</div>

<div class="foot-contact" style="left:876px;top:3003px;width:230px">©<b>DR.LUMORA</b> - 2016, All rights resreved.</div>

</body>
</html>
```